Web page design for podiatry office*

Need a web page for our podiatry office. It should feature most of our services, hours, directions and location. Should include a short bio of the doctor and a contact page.

Coding

Coded - Design and coding required

Number of Pages Required

1 page

Colors

Designer to choose colors to be used in the design.

```html
<!DOCTYPE html>
<html lang="en">
<head>
<meta charset="utf-8">
<title>Stride Foot Clinic — Podiatry</title>
<link rel="stylesheet" href="https://fonts.googleapis.com/css2?family=Nunito+Sans:wght@400;600;700&display=swap">
<style>
  :root{
    --navy:#1b2541;
    --navy-deep:#141b2e;
    --field:#151b2c;
    --blue:#0d94f5;
    --nav-active:#cfe8fb;
    --ink:#1a1f2b;
    --ink-soft:#3a3f4a;
    --white:#ffffff;
  }
  *{box-sizing:border-box;margin:0;padding:0}
  html,body{width:1200px;height:3154px;overflow:hidden}
  body{position:relative;font-family:"Nunito Sans",Arial,sans-serif;color:var(--ink);background:var(--white)}
  .abs{position:absolute}
  .btn{position:absolute;background:var(--blue);color:var(--white);font-size:14px;display:flex;align-items:center;justify-content:center;letter-spacing:.3px;text-transform:uppercase}

  /* header */
  .site-header{position:absolute;left:0;top:0;width:1200px;height:86px;background:var(--white)}
  .brand{position:absolute;left:98px;top:26px;display:flex;align-items:center;gap:10px;font-weight:700;font-size:19px;color:var(--navy)}
  .brand-dot{width:28px;height:28px;border-radius:50%;background:var(--blue)}
  .nav a{position:absolute;top:0;height:86px;display:flex;align-items:center;font-size:14px;color:var(--ink-soft);text-decoration:none;letter-spacing:.4px}
  .nav .active{background:var(--nav-active);justify-content:center;width:76px;left:579px}

  /* hero */
  .hero-photo{position:absolute;left:0;top:86px;width:1200px;height:682px;background:linear-gradient(120deg,#b9b3ad 0%,#d6c9bf 35%,#c8a48d 60%,#e3d8cf 80%,#a9a29d 100%)}
  .hero-panel{position:absolute;left:0;top:231px;width:584px;height:391px;background:var(--navy);color:var(--white)}
  .hero-title{position:absolute;left:98px;top:40px;font-size:36px;font-weight:600;line-height:44px}
  .hero-title span{color:var(--blue);display:block}
  .hero-text{position:absolute;left:98px;top:138px;font-size:15.5px;line-height:22px}
  .hero-info{position:absolute;top:228px;font-size:14px;line-height:22px}

  /* services */
  .section-title{position:absolute;left:0;width:1200px;text-align:center;font-size:27px;font-weight:600;color:var(--navy)}
  .section-lead{position:absolute;left:0;width:1200px;text-align:center;font-size:15.5px;line-height:20px}
  .service-card{position:absolute;top:951px;width:317px}
  .service-image{width:317px;height:163px;background:linear-gradient(90deg,#cfcdd1,#c8c5c9 50%,#d3d1d4)}
  .service-card h3{font-size:18px;font-weight:600;margin-top:17px;color:var(--ink)}
  .service-card p{font-size:13.5px;line-height:19px;margin-top:8px;color:var(--ink-soft)}

  /* cta band */
  .cta-band{position:absolute;left:0;top:1287px;width:1200px;height:77px;background:var(--navy);color:var(--white)}
  .cta-band p{position:absolute;left:97px;top:27px;font-size:18px}

  /* doctor */
  .doctor-band{position:absolute;left:0;top:1523px;width:557px;height:230px;background:var(--navy)}
  .doctor-photo{position:absolute;left:192px;top:1425px;width:311px;height:428px;background:linear-gradient(180deg,#8fb5d6 0%,#a7c6df 45%,#e7ecf1 75%,#cfd7df 100%);box-shadow:0 2px 6px rgba(0,0,0,.25)}
  .doctor-name{position:absolute;left:614px;top:1530px;font-size:29px;font-weight:600;color:var(--navy)}
  .doctor-lead{position:absolute;left:614px;top:1574px;font-size:15.5px;line-height:20px}
  .doctor-bio{position:absolute;left:614px;top:1632px;width:470px;font-size:13.5px;line-height:21.5px;color:var(--ink-soft)}

  /* location */
  .map{position:absolute;left:0;top:1957px;width:784px;height:480px;background:linear-gradient(135deg,#eceeef,#f5f5f5 50%,#e4e6e8)}
  .location-panel{position:absolute;left:784px;top:1957px;width:416px;height:480px;background:var(--navy);color:var(--white)}
  .location-panel p{position:absolute;left:86px;top:212px;font-size:18px;line-height:24px}

  /* contact */
  .contact{position:absolute;left:0;top:2512px;width:1200px;height:574px;background:var(--navy);color:var(--white)}
  .contact .section-title{color:var(--white)}
  .field-label{position:absolute;font-size:12.5px}
  .field{position:absolute;background:var(--field)}

  /* footer */
  .site-footer{position:absolute;left:0;top:3086px;width:1200px;height:68px;background:var(--navy-deep);color:var(--white)}
  .site-footer p{position:absolute;left:98px;top:24px;font-size:13.5px}
  .social{position:absolute;top:27px;width:15px;height:15px;border-radius:50%;background:var(--white)}
</style>
</head>
<body>

<header class="site-header">
  <div class="brand"><span class="brand-dot"></span>Stride Foot Clinic</div>
  <nav class="nav">
    <a class="active" href="#">HOME</a>
    <a href="#" style="left:681px">SERVICES</a>
    <a href="#" style="left:786px">ABOUT</a>
    <a href="#" style="left:874px">CONTACT</a>
  </nav>
  <a class="btn" href="#" style="left:989px;top:27px;width:112px;height:31px">Book Now</a>
</header>

<section class="hero">
  <div class="hero-photo" role="img" aria-label="Photograph of bare feet resting on a sunlit rock"></div>
  <div class="hero-panel">
    <h1 class="hero-title">Foot or Ankle Pain ?<span>We’re here for you !</span></h1>
    <p class="hero-text">Lorem ipsum dolor sit amet, consectetur adipiscing elit.<br>Integer ullamcorper arcu eu lorem interdum.</p>
    <svg class="abs" style="left:98px;top:228px" width="22" height="30" viewBox="0 0 22 30"><path d="M11 0C5 0 0 5 0 11c0 8 11 19 11 19s11-11 11-19C22 5 17 0 11 0z" fill="#fff"/><circle cx="11" cy="11" r="4" fill="#1b2541"/></svg>
    <svg class="abs" style="left:311px;top:228px" width="30" height="30" viewBox="0 0 30 30"><circle cx="15" cy="15" r="14" fill="#fff"/><path d="M15 7v8h6" stroke="#1b2541" stroke-width="1.6" fill="none"/></svg>
    <p class="hero-info" style="left:98px;top:270px">48 Alder Lane<br>Fairview, NH</p>
    <p class="hero-info" style="left:311px;top:270px">9 AM to 7PM<br>Monday - Friday</p>
  </div>
  <a class="btn" href="#" style="left:251px;top:601px;width:164px;height:37px;gap:14px">Book Now
    <svg width="20" height="12" viewBox="0 0 20 12"><path d="M0 6h18M13 1l5 5-5 5" stroke="#fff" stroke-width="1.6" fill="none"/></svg></a>
</section>

<section class="services">
  <h2 class="section-title" style="top:826px">OUR SERVICES</h2>
  <p class="section-lead" style="top:874px">Lorem ipsum dolor sit amet, consectetur adipiscing elit.<br>Integer ullamcorper arcu eu lorem interdum.</p>
  <article class="service-card" style="left:98px">
    <div class="service-image" role="img" aria-label="Anatomical model of a foot"></div>
    <h3>Lorem ipsum dolor</h3>
    <p>Lorem ipsum dolor sit amet, consectetur adipiscing elit. Integer ullamcorper arcu eu lorem interdum vehicula. Fusce hendrerit auctor urna vitae lobortis. Praesent nec euismod velit, at placerat tortor.</p>
  </article>
  <article class="service-card" style="left:441px">
    <div class="service-image" role="img" aria-label="Anatomical model of a foot"></div>
    <h3>Lorem ipsum dolor</h3>
    <p>Lorem ipsum dolor sit amet, consectetur adipiscing elit. Integer ullamcorper arcu eu lorem interdum vehicula. Fusce hendrerit auctor urna vitae lobortis. Praesent nec euismod velit, at placerat tortor.</p>
  </article>
  <article class="service-card" style="left:784px">
    <div class="service-image" role="img" aria-label="Anatomical model of a foot"></div>
    <h3>Lorem ipsum dolor</h3>
    <p>Lorem ipsum dolor sit amet, consectetur adipiscing elit. Integer ullamcorper arcu eu lorem interdum vehicula. Fusce hendrerit auctor urna vitae lobortis. Praesent nec euismod velit, at placerat tortor.</p>
  </article>
</section>

<section class="cta-band">
  <p>Add text here to make the user want to click the button on right ?</p>
  <a class="btn" href="#" style="left:964px;top:21px;width:137px;height:35px">Contact Now</a>
</section>

<section class="doctor">
  <div class="doctor-band"></div>
  <div class="doctor-photo" role="img" aria-label="Portrait of the doctor in a white coat"></div>
  <h2 class="doctor-name">JOHN DOE</h2>
  <p class="doctor-lead">Lorem ipsum dolor sit amet, consectetur adipiscing elit.<br>Integer ullamcorper arcu eu lorem interdum.</p>
  <p class="doctor-bio">Integer blandit ultricies aliquam. Pellentesque quis dui varius, dapibus velit id, iaculis ipsum. Morbi ac eros feugiat, lacinia elit ut, elem turpis.Curabitur justo sapien, tempus sit amet rutrum eu, commodo eu lacus. Morbi in ligula nibh. Maecenas ut mi at odio hendrerit eleifend tempor.<br>justo sapien, tempus</p>
</section>

<section class="location">
  <div class="map" role="img" aria-label="Street map showing the clinic location"></div>
  <div class="location-panel">
    <svg class="abs" style="left:86px;top:150px" width="30" height="42" viewBox="0 0 22 30"><path d="M11 0C5 0 0 5 0 11c0 8 11 19 11 19s11-11 11-19C22 5 17 0 11 0z" fill="#fff"/><circle cx="11" cy="11" r="4" fill="#1b2541"/></svg>
    <p>48 Alder Lane<br>Fairview, NH</p>
    <a class="btn" href="#" style="left:86px;top:292px;width:139px;height:36px">Get Directions</a>
  </div>
</section>

<section class="contact">
  <h2 class="section-title" style="top:62px">CONTACT US</h2>
  <p class="section-lead" style="top:109px">Lorem ipsum dolor sit amet, consectetur adipiscing elit.<br>Integer ullamcorper arcu eu lorem interdum.</p>
  <label class="field-label" style="left:269px;top:192px">Enter full name</label>
  <div class="field" style="left:269px;top:216px;width:315px;height:36px"></div>
  <label class="field-label" style="left:610px;top:192px">Enter email Id</label>
  <div class="field" style="left:610px;top:216px;width:317px;height:36px"></div>
  <label class="field-label" style="left:269px;top:275px">Message</label>
  <div class="field" style="left:269px;top:298px;width:660px;height:147px"></div>
  <a class="btn" href="#" style="left:527px;top:482px;width:145px;height:33px">Send Message</a>
</section>

<footer class="site-footer">
  <p>Copyright © Stride Foot Clinic.</p>
  <span class="social" style="left:976px" aria-label="Social link"></span>
  <span class="social" style="left:1010px" aria-label="Social link"></span>
  <span class="social" style="left:1047px" aria-label="Social link"></span>
  <span class="social" style="left:1086px" aria-label="Social link"></span>
</footer>

</body>
</html>
```